Association le rameau de Tiburel needs a web design design

hello I would like to redo the website of my charity for it to be clearer and more profesional,our association is involved in a orphanage in haiti in port- au-prince here is the first site I did, but it is not very pretty or very credible.

http://rametiburel.sitevela.org/ramet

Industry/Entity Type

Charity

```html
<!DOCTYPE html>
<html lang="fr">
<head>
<meta charset="utf-8">
<title>Rametiburel</title>
<link href="https://fonts.googleapis.com/css2?family=Raleway:wght@400;500;600&family=Open+Sans:wght@400;600&display=swap" rel="stylesheet">
<style>
:root{
  --magenta:#a6387f;
  --magenta-light:#c3559f;
  --magenta-dark:#9a2f76;
  --gold:#e2aa0c;
  --green:#7aae14;
  --text:#444;
  --muted:#7a7a7a;
  --footer:#e6e6e6;
  --panel:#f4f4f4;
}
*{margin:0;padding:0;box-sizing:border-box}
html,body{width:915px;height:1200px;overflow:hidden;background:#fff}
body{position:relative;font-family:"Open Sans",sans-serif;color:var(--text)}
.abs{position:absolute}
.brand{left:97px;top:26px;font-family:"Raleway",sans-serif;font-size:31px;color:var(--magenta);font-weight:400}
.nav{left:95px;top:75px;width:725px;height:37px;background:linear-gradient(var(--magenta-light),var(--magenta-dark));display:flex}
.nav a{font-family:"Raleway",sans-serif;font-weight:600;font-size:11px;color:#fff;text-decoration:none;display:flex;align-items:center;justify-content:center;border-right:1px solid rgba(0,0,0,.18)}
.hero{left:95px;top:112px;width:725px;height:297px;background:linear-gradient(90deg,#5c6b3a 0%,#7d8a4a 35%,#5a4a3a 55%,#c9a27c 70%,#8a7f5a 100%)}
.hero-box{left:130px;top:190px;width:288px;height:126px;background:rgba(226,170,12,.93);padding:22px 23px;color:#fff}
.hero-box .kicker{font-family:"Raleway",sans-serif;font-size:17px}
.hero-box h1{font-family:"Raleway",sans-serif;font-weight:400;font-size:23px;margin-top:1px}
.hero-box p{font-size:9px;line-height:14px;margin-top:6px}
.dots{left:432px;top:384px;width:52px;height:25px;background:rgba(60,50,40,.7);border-radius:14px 14px 0 0;display:flex;gap:3px;justify-content:center;align-items:center;padding-top:2px}
.dots span{width:9px;height:9px;border-radius:50%;background:#fff}
.welcome{left:94px;top:452px;width:400px}
.welcome h2{font-family:"Raleway",sans-serif;font-weight:400;font-size:22px;color:#333}
.welcome h3{font-family:"Raleway",sans-serif;font-weight:400;font-size:16px;color:#333;margin-top:6px}
.welcome p{font-size:7.6px;line-height:14px;color:#555;margin-top:10px}
.welcome p+p{margin-top:3px}
.welcome-photo{left:553px;top:442px;width:254px;height:148px;background:linear-gradient(135deg,#b8723d,#d9914e 60%,#a9683a)}
.goals{left:0;top:638px;width:915px;height:269px;background:var(--green);color:#fff}
.goals h2{position:absolute;top:34px;width:100%;text-align:center;font-family:"Raleway",sans-serif;font-weight:400;font-size:23px}
.goal{position:absolute;top:90px;width:180px;text-align:center}
.goal .ring{width:71px;height:71px;border:2px solid #fff;border-radius:50%;margin:0 auto;display:flex;align-items:center;justify-content:center}
.goal h4{font-family:"Raleway",sans-serif;font-weight:500;font-size:13px;margin-top:13px}
.goal p{font-size:8px;line-height:12.5px;margin-top:4px;color:#eef6dc}
.recent-title{left:94px;top:944px;font-family:"Raleway",sans-serif;font-weight:500;font-size:18px;color:var(--magenta)}
.panel{left:576px;top:980px;width:235px;height:138px;background:var(--panel)}
.post-img{top:984px;width:100px;height:81px}
.post{top:983px;width:125px}
.post h5{font-family:"Raleway",sans-serif;font-weight:400;font-size:10.5px;color:#444}
.post p{font-size:7.6px;line-height:13.5px;color:var(--muted);margin-top:3px}
.post a{font-size:8px;color:var(--green);text-decoration:none;display:block;margin-top:1px}
.footer{left:0;top:1118px;width:915px;height:82px;background:var(--footer)}
.foot-links{left:98px;top:1144px;font-family:"Raleway",sans-serif;font-weight:600;font-size:10px;color:#222}
.foot-links span{margin:0 4px}
.copy{left:98px;top:1163px;font-size:7.5px;color:#333}
.social{left:760px;top:1145px;display:flex;gap:9px}
.social span{width:13px;height:13px;border-radius:50%;background:#444}
</style>
</head>
<body>
<div class="abs brand">Rametiburel</div>
<nav class="abs nav">
  <a style="width:94px">ACCUEIL</a>
  <a style="width:111px">L'ASSOCIATION</a>
  <a style="width:107px">L'ORPHELINAT</a>
  <a style="width:95px">ACTUALITES</a>
  <a style="width:97px">DONATIONS</a>
  <a style="width:82px;border:none">CONTACT</a>
</nav>
<div class="abs hero" role="img" aria-label="Photo of a volunteer smiling with two children outdoors"></div>
<div class="abs hero-box">
  <div class="kicker">Lorem ipsum dolor amet</div>
  <h1>Nullam Enimleo egest</h1>
  <p>Mauris vel lacus vitae felis vestibulum volutpat Etiam est nunc venenatis in tristique eu imperdiet ac</p>
</div>
<div class="abs dots"><span></span><span></span><span></span><span></span></div>

<section class="abs welcome">
  <h2>Welcome to the website of the</h2>
  <h3>Association Rameau orphanage in Tiburel</h3>
  <p>L'association RAMET est une structure non lucrative établie à Genève, afin de soutenir l' Orphelinat le Rameau à Tiburel.créé au lendemain du séisme du 12 janvier 2010.</p>
  <p>&nbsp;L'orphelinat et l'association souhaitent apporter leur aide à une partie des quelques 100 000 enfants orphelins que compte le pays suite à cette catastrophe.</p>
</section>
<div class="abs welcome-photo" role="img" aria-label="Photo of a small child sitting with an adoption sign"></div>

<section class="abs goals">
  <h2>The goals of the Association</h2>
  <div class="goal" style="left:95px">
    <div class="ring"><svg width="38" height="32" viewBox="0 0 38 32" fill="#fff"><path d="M12 2l7 3-7 3-7-3z M5 6l7 3v7l-7-3z M13 9l7-3v7l-7 3z"/><path d="M7 16l7 3-7 3-7-3z M0 20l7 3v7l-7-3z M8 23l7-3v7l-7 3z" transform="translate(2 0)"/><path d="M25 16l7 3-7 3-7-3z M18 20l7 3v7l-7-3z M26 23l7-3v7l-7 3z" transform="translate(2 0)"/></svg></div>
    <h4>Provide logistical support</h4>
    <p>Nibh ligula pulvinar metus eget consectetuer augue nisi quis lacus Ut ac mi quis lacus mollis aliquam Curabitur</p>
  </div>
  <div class="goal" style="left:273px">
    <div class="ring"><svg width="38" height="28" viewBox="0 0 38 28" fill="#fff"><path d="M19 2l18 7-18 7L1 9z"/><path d="M9 14v7c3 3 17 3 20 0v-7l-10 4z"/><rect x="33" y="10" width="1.6" height="11"/></svg></div>
    <h4>Medical &amp; Education</h4>
    <p>Nibh ligula pulvinar metus eget consectetuer augue nisi quis lacus Ut ac mi quis lacus mollis aliquam Curabitur iaculis</p>
  </div>
  <div class="goal" style="left:458px">
    <div class="ring"><svg width="30" height="30" viewBox="0 0 30 30" fill="#fff"><path d="M8 4c3-3 7 1 7 5 0-4 4-8 7-5 2 2 0 5-3 5h-8c-3 0-5-3-3-5z"/><rect x="2" y="10" width="26" height="6"/><rect x="4" y="17" width="22" height="11"/><rect x="13" y="10" width="4" height="18" fill="var(--green)"/></svg></div>
    <h4>Donation to Orphanage</h4>
    <p>Nibh ligula pulvinar metus eget consectetuer augue nisi quis lacus Ut ac mi quis lacus mollis aliquam Curabitur</p>
  </div>
  <div class="goal" style="left:637px">
    <div class="ring"><svg width="30" height="32" viewBox="0 0 30 32" fill="#fff"><circle cx="15" cy="9" r="8"/><path d="M1 32c0-10 5-14 14-14s14 4 14 14z"/></svg></div>
    <h4>Website Monitor</h4>
    <p>Nibh ligula pulvinar metus eget consectetuer augue nisi quis lacus Ut ac mi quis lacus mollis aliquam Curabit</p>
  </div>
</section>

<h2 class="abs recent-title">Recent Donation &amp; Blogs</h2>
<div class="abs panel"></div>

<div class="abs post-img" style="left:95px;background:linear-gradient(135deg,#8a5a3a,#c49a74)" role="img" aria-label="Photo of a group of children sitting together"></div>
<div class="abs post" style="left:205px">
  <h5>Morbi ornare gravida</h5>
  <p>Cum sociis natoque penatibus et magnis dis parturient montes nascetur ridiculus mus In iaculis facilisis massa sed luctus</p>
  <a>READ MORE</a>
</div>
<div class="abs post-img" style="left:342px;background:linear-gradient(135deg,#3a3a3a,#9a9a9a)" role="img" aria-label="Black and white photo of a baby"></div>
<div class="abs post" style="left:451px">
  <h5>Morbi ornare gravida</h5>
  <p>Cum sociis natoque penatibus et magnis dis parturient montes nascetur ridiculus mus In iaculis facilisis massa sed luctus</p>
  <a>READ MORE</a>
</div>
<div class="abs post-img" style="left:588px;background:linear-gradient(135deg,#d9d2c4,#b87a52 55%,#e0b23a)" role="img" aria-label="Photo of many hands stacked together"></div>
<div class="abs post" style="left:700px">
  <h5>Morbi ornare gravida</h5>
  <p>Cum sociis natoque penatibus et magnis dis parturient montes nascetur ridiculus mus In iaculis facilisis massa sed luctus</p>
  <a>READ MORE</a>
</div>

<footer class="abs footer"></footer>
<div class="abs foot-links">ACCUEIL<span>|</span>L'ASSOCIATION<span>|</span>L'ORPHELINAT<span>|</span>ACTUALITES<span>|</span>DONATIONS<span>|</span>CONTACT</div>
<div class="abs copy">© 2015 Company Name &nbsp;All right reserved &nbsp;Term of Use</div>
<div class="abs social" aria-label="Social links"><span></span><span></span><span></span></div>
</body>
</html>
```